Tamkor, a service provider dedicated to improving the performance of a website

Tamkor offers optimization and performance improvement for all types of websites (showcase sites, e-commerce, ...), with the aim of improving their ranking on Vintrel and their customer transformation rate. The main benefits consist in optimizing the factors of a site. In addition, we also offer content creation (description of product sheets, services, ...), Vintrel Ads campaign management, migration version for Prestashop / Wordpress, etc. The design must be a fresh image, dynamic, why not "fun", but also serious. No favorite color, carte blanche on this point;)

```html
<!DOCTYPE html>
<html lang="en">
<head>
<meta charset="utf-8">
<title>Tamkor business card</title>
<link rel="stylesheet" href="https://fonts.googleapis.com/css2?family=Poppins:wght@700&family=Roboto:wght@400;700&display=swap">
<style>
  :root {
    --bg: #2b2b2d;
    --card-white: #ffffff;
    --card-black: #1b1b1c;
    --brand-blue: #3d55a8;
    --text-dark: #1e1e22;
    --icon-blue: #3d55a8;
  }
  * { box-sizing: border-box; margin: 0; padding: 0; }
  html, body { width: 1200px; height: 960px; overflow: hidden; }
  body {
    background: var(--bg);
    font-family: "Roboto", Arial, sans-serif;
    position: relative;
  }
  .card {
    position: absolute;
    left: 250px;
    width: 700px;
    height: 400px;
    border-radius: 26px;
    overflow: hidden;
  }
  .card-back { top: 40px; background: var(--card-black); }
  .card-front { top: 520px; background: var(--card-white); }

  .brand-tile {
    position: absolute;
    background: var(--brand-blue);
    display: flex;
    align-items: center;
    justify-content: center;
  }
  .card-back .brand-tile {
    width: 210px; height: 210px; left: 245px; top: 95px; border-radius: 56px;
  }
  .brand-tile-name {
    font-family: "Poppins", Arial, sans-serif;
    font-weight: 700;
    color: #ffffff;
    font-size: 40px;
  }
  .card-front .brand-tile {
    width: 330px; height: 330px; left: 340px; top: 35px; border-radius: 90px;
  }

  .wordmark {
    position: absolute;
    left: 40px; top: 70px;
    font-family: "Poppins", Arial, sans-serif;
    font-weight: 700;
    font-size: 60px;
    line-height: 1;
    color: var(--brand-blue);
  }
  .person { position: absolute; left: 44px; top: 170px; }
  .person-name {
    font-family: "Poppins", Arial, sans-serif;
    font-weight: 700;
    font-size: 24px;
    color: var(--brand-blue);
    line-height: 1.1;
  }
  .person-role { font-size: 17px; color: var(--text-dark); margin-left: 14px; }
  .address {
    position: absolute; left: 58px; top: 240px;
    font-size: 16px; line-height: 1.3; color: var(--text-dark);
    font-style: normal;
  }
  .contacts { position: absolute; left: 58px; top: 300px; list-style: none; }
  .contacts li {
    display: flex; align-items: center; gap: 8px;
    font-size: 16px; line-height: 1.35; color: var(--text-dark);
  }
  .contacts svg { width: 13px; height: 13px; fill: var(--icon-blue); flex: none; }
</style>
</head>
<body>
  <section class="card card-back">
    <div class="brand-tile"><span class="brand-tile-name">Tamkor</span></div>
  </section>

  <section class="card card-front">
    <div class="wordmark">Tamkor</div>
    <div class="person">
      <div class="person-name">Daniel Reyes</div>
      <div class="person-role">Owner</div>
    </div>
    <address class="address">410-226 Harbour Lane<br>Northgate, BC, V2K 4R</address>
    <ul class="contacts">
      <li>
        <svg viewBox="0 0 16 16" aria-hidden="true"><path d="M3 1h3l1.5 4-2 1.2a9 9 0 0 0 4.3 4.3L11 8.5l4 1.5v3a2 2 0 0 1-2 2A12 12 0 0 1 1 3a2 2 0 0 1 2-2z"/></svg>
        555-271-0938
      </li>
      <li>
        <svg viewBox="0 0 16 16" aria-hidden="true"><path d="M1 3h14v10H1z M1 3l7 6 7-6" stroke="#fff" stroke-width="1.2"/></svg>
        hello@tamkor-mail.com
      </li>
      <li>
        <svg viewBox="0 0 16 16" aria-hidden="true"><circle cx="8" cy="8" r="7"/><path d="M1 8h14M8 1c3 3 3 11 0 14M8 1c-3 3-3 11 0 14" stroke="#fff" stroke-width="1" fill="none"/></svg>
        www.tamkor-site.com
      </li>
    </ul>
    <div class="brand-tile"></div>
  </section>
</body>
</html>
```